Business card for denture clinic Gumlyssa

We need a new business card with our new logo. We are a denture clinic in New Zealand with our target market being 45+ years old. We would need a space on the back to write our patients next appointment on. We would space for only one appointment rather than a list. We will attach a photo showing an example of this. But of course, we would like to see your twist on this. We want it to be bold and easy to read and a good mixture of professional but modern. We have attached our logo to be used on the card.

Target Market(s)

People aged 45+ needing dentures

Industry/Entity Type

Dental

Contact Information for Business Card

We want our logo on the front and the space to write an appointment on the back. I've attached an example our our old business card showing this. We need to have the technicians details on the front.

Font styles to use
Sans Serif

Colors
0255a3
919191
fbfbfb

Requirements
Must have
• The following details:
• Ravi Pelling BDT, PGDipCDentTech Marlow
• Dental Prosthetist
• Phone numbers: 0800 47 2150
• 09 571 3294
• Email: ravi@gumlyssa.co.nz
• www.gumlyssa.co.nz
• Address: 418 Whiroa Road
• Kauriwhenua East
• Auckland 0610
Nice to have
• We would like our business cards to have more than just two colours as we want them to be more vibrant. We have uploaded an example of a business card we liked that showed this.

```html
<!DOCTYPE html>
<html lang="en">
<head>
<meta charset="utf-8">
<title>Gumlyssa – Business Card</title>
<link rel="stylesheet" href="https://fonts.googleapis.com/css2?family=Exo+2:wght@400;500;600;700;800&display=swap">
<style>
  :root {
    --brand-blue: #0a6dba;
    --paper: #ffffff;
    --backdrop: #eceef1;
    --ink-light: #ffffff;
    --shadow: rgba(20, 40, 70, 0.18);
  }
  * { box-sizing: border-box; margin: 0; padding: 0; }
  html, body {
    width: 1200px; height: 900px; overflow: hidden;
    background: var(--backdrop);
    font-family: "Exo 2", sans-serif;
  }
  .canvas { position: relative; width: 1200px; height: 900px; }

  .card {
    position: absolute;
    width: 556px; height: 342px;
    border-radius: 36px;
    overflow: hidden;
    background: var(--paper);
    box-shadow: 0 10px 30px var(--shadow);
    display: flex;
  }
  .card--front { left: 238px; top: 62px; }
  .card--back  { left: 460px; top: 519px; }

  .card__brand-side {
    position: relative;
    width: 267px;
    background: var(--paper);
  }

  .card__info-side {
    position: relative;
    flex: 1;
    background: var(--brand-blue);
    color: var(--ink-light);
  }

  /* Brand lockup */
  .brand {
    position: absolute;
    left: 0; right: 0;
    display: flex; flex-direction: column; align-items: center;
  }
  .card--front .brand { top: 131px; }
  .card--back  .brand { top: 123px; }
  .brand__mark {
    width: 44px; height: 44px;
    background: var(--brand-blue);
  }
  .brand__name {
    margin-top: 6px;
    font-size: 25px;
    font-weight: 600;
    letter-spacing: 0.5px;
    text-transform: uppercase;
    color: var(--brand-blue);
    line-height: 1;
  }

  /* Front details */
  .person { position: absolute; left: 21px; top: 56px; }
  .person__name {
    font-size: 26px; font-weight: 800; letter-spacing: 1.5px;
    text-transform: uppercase; line-height: 1;
  }
  .person__post { font-size: 14px; font-weight: 500; letter-spacing: 0.5px; }
  .person__quals { margin-top: 6px; font-size: 15px; font-weight: 400; }
  .person__role { margin-top: 4px; font-size: 15.5px; font-weight: 600; }

  .contacts { position: absolute; left: 21px; top: 149px; list-style: none; }
  .contacts li {
    display: flex; align-items: center; gap: 10px;
    font-size: 15.5px; height: 25px;
  }
  .contacts svg { width: 13px; height: 13px; flex: none; }

  .address {
    position: absolute; left: 22px; top: 247px;
    font-style: normal; font-size: 15.5px; line-height: 20px;
  }
  .website {
    position: absolute; left: 22px; top: 292px;
    font-size: 15.5px; font-weight: 600; line-height: 20px;
  }

  /* Back appointment */
  .appointment { position: absolute; left: 24px; top: 112px; }
  .appointment__title { font-size: 20px; font-weight: 600; letter-spacing: 0.2px; }
  .appointment__row {
    display: flex; align-items: center; margin-top: 13px;
  }
  .appointment__row:first-of-type { margin-top: 22px; }
  .appointment__label { width: 69px; font-size: 17px; font-weight: 400; }
  .appointment__field {
    width: 161px; height: 26px;
    background: var(--paper); border-radius: 5px;
  }
</style>
</head>
<body>
<main class="canvas">

  <section class="card card--front" aria-label="Business card front">
    <div class="card__brand-side">
      <div class="brand">
        <span class="brand__mark"></span>
        <span class="brand__name">Gumlyssa</span>
      </div>
    </div>
    <div class="card__info-side">
      <div class="person">
        <p class="person__name">Ravi Pelling <span class="person__post">BDT,</span></p>
        <p class="person__quals">PGDipCDentTech Marlow</p>
        <p class="person__role">Dental Prosthetist</p>
      </div>
      <ul class="contacts">
        <li>
          <svg viewBox="0 0 13 13" aria-hidden="true"><rect width="13" height="13" rx="2" fill="#fff"/><path d="M3 4.5c0-1 1-1.5 3.5-1.5S10 3.5 10 4.5v1H8.2V4.6H4.8v.9H3zM4 6.5h5l1 3.5H3z" fill="#0a6dba"/></svg>
          <span>0800 47 2150</span>
        </li>
        <li>
          <svg viewBox="0 0 13 13" aria-hidden="true"><rect width="13" height="13" rx="2" fill="#fff"/><path d="M3 4.5c0-1 1-1.5 3.5-1.5S10 3.5 10 4.5v1H8.2V4.6H4.8v.9H3zM4 6.5h5l1 3.5H3z" fill="#0a6dba"/></svg>
          <span>09 571 3294</span>
        </li>
        <li>
          <svg viewBox="0 0 13 13" aria-hidden="true"><rect width="13" height="13" rx="2" fill="#fff"/><rect x="2.5" y="3.5" width="8" height="6" fill="none" stroke="#0a6dba" stroke-width="1"/><path d="M2.5 3.5l4 3.2 4-3.2" fill="none" stroke="#0a6dba" stroke-width="1"/></svg>
          <span>ravi@gumlyssa.co.nz</span>
        </li>
      </ul>
      <address class="address">
        418 Whiroa Road<br>
        Kauriwhenua East Auckland 0610
      </address>
      <p class="website">www.gumlyssa.co.nz</p>
    </div>
  </section>

  <section class="card card--back" aria-label="Business card back">
    <div class="card__brand-side">
      <div class="brand">
        <span class="brand__mark"></span>
        <span class="brand__name">Gumlyssa</span>
      </div>
    </div>
    <div class="card__info-side">
      <div class="appointment">
        <p class="appointment__title">Your next appointment</p>
        <div class="appointment__row">
          <span class="appointment__label">Date</span>
          <span class="appointment__field"></span>
        </div>
        <div class="appointment__row">
          <span class="appointment__label">Time</span>
          <span class="appointment__field"></span>
        </div>
      </div>
    </div>
  </section>

</main>
</body>
</html>
```